RVT studios

rvt studios is an interior design firm in omaha, NE. Offering complete residential/commercial design. Exterior, int finishes, cabinets, furniture, window covering. Have been in business for 25 yrs. Lived in and/or completed work in LA, NYC, PHX, MIami, London, Canada, Mexico. We would like to see a marketing flyer with clean, architectural design. Modern .Flyer will be on display at open houses & mailed to perspective clients. Dont want a lot of color. Prefer whites/black, greys or brown. Maybe small accent of blue like logo. Block architectural lettering. do not need to use all photos. but use at least one from each of the three projects. thanks for you time

please change/add on any and all submissions the following add: Dana Whitcombe, Principal (in info section not on logo) change: Info@rvtstudios.com, not dana @rvtstudios.com add: back design, would like to use as many photos as possible thanks you

```html
<!DOCTYPE html>
<html lang="en">
<head>
<meta charset="utf-8">
<title>RVT studios – Interior design firm in Omaha, NE</title>
<link rel="stylesheet" href="https://fonts.googleapis.com/css2?family=Crimson+Text&family=Alegreya:ital,wght@1,400;1,700&family=Questrial&family=Open+Sans:ital,wght@1,700&display=swap">
<style>
  :root {
    --brown-dark: #4a3427;
    --brown-tan: #c3a07b;
    --paper: #ffffff;
    --text-grey: #505050;
    --page-bg: #e9e6e2;
  }
  * { margin: 0; padding: 0; box-sizing: border-box; }
  html, body {
    width: 1200px; height: 806px; overflow: hidden;
    background: var(--page-bg);
  }
  .flyer {
    position: relative;
    width: 1200px; height: 806px;
    background: var(--paper);
    overflow: hidden;
  }
  .header-shapes, .footer-shapes {
    position: absolute; left: 0; display: block;
  }
  .header-shapes { top: 0; }
  .footer-shapes { top: 734px; }

  .brand {
    position: absolute; left: 53px; top: 48px;
    color: var(--paper);
    font-family: "Crimson Text", Georgia, serif;
  }
  .brand-name {
    font-size: 92px; line-height: 1; letter-spacing: 1px;
  }
  .brand-tagline {
    margin-top: 6px;
    font-size: 32px; line-height: 1;
  }

  .headline {
    position: absolute; right: 55px; top: 66px;
    text-align: right;
    font-family: "Alegreya", Georgia, serif;
    font-style: italic;
  }
  .headline-main {
    color: var(--brown-dark);
    font-weight: 700; font-size: 50px; line-height: 1.1;
  }
  .headline-place {
    color: var(--brown-tan);
    font-weight: 400; font-size: 50px; line-height: 1.15;
  }

  .gallery {
    position: absolute; left: 53px; top: 254px;
    display: flex; gap: 14px;
  }
  .gallery-photo { width: 263px; height: 256px; }
  .photo-library { background: linear-gradient(135deg, #e8e2d6, #b9a98f 55%, #5b4a3b); }
  .photo-kitchen { background: linear-gradient(160deg, #efe6d3, #cdb28a 50%, #6a5240); }
  .photo-bath    { background: linear-gradient(180deg, #1c1c1c, #4a4a4a 45%, #d6d6d4); }
  .photo-wine    { background: linear-gradient(120deg, #3a2a20, #8a6a4e 50%, #2a1d15); }

  .about {
    position: absolute; left: 53px; top: 532px; width: 1094px;
    font-family: "Questrial", "Century Gothic", sans-serif;
    font-size: 21.5px; line-height: 30px;
    color: var(--text-grey);
    text-align: justify;
  }
  .about p + p { margin-top: 28px; }

  .contact {
    position: absolute; top: 734px; height: 72px;
    display: flex; align-items: center; gap: 12px;
    color: var(--paper);
    font-family: "Open Sans", Arial, sans-serif;
    font-style: italic; font-weight: 700; font-size: 25px;
  }
  .contact-phone { left: 53px; }
  .contact-email { left: 414px; }
  .contact-web   { left: 782px; }
  .contact svg { flex: none; }
</style>
</head>
<body>
<main class="flyer">
  <svg class="header-shapes" width="1200" height="230" viewBox="0 0 1200 230" aria-hidden="true">
    <polygon points="0,0 667,0 568,228 0,228" fill="var(--brown-dark)"/>
    <polygon points="660,0 1200,0 1200,27 648,27" fill="var(--brown-tan)"/>
  </svg>

  <div class="brand">
    <div class="brand-name">RVT studios</div>
    <div class="brand-tagline">Complete Design</div>
  </div>

  <div class="headline">
    <div class="headline-main">Interior design firm</div>
    <div class="headline-place">in omaha, NE</div>
  </div>

  <section class="gallery">
    <div class="gallery-photo photo-library" role="img" aria-label="Photo of a white built-in library with bookshelves and arched doorway"></div>
    <div class="gallery-photo photo-kitchen" role="img" aria-label="Photo of a cream kitchen with range hood and gas cooktop"></div>
    <div class="gallery-photo photo-bath" role="img" aria-label="Photo of a dark modern bathroom with freestanding tub and marble floor"></div>
    <div class="gallery-photo photo-wine" role="img" aria-label="Photo of a stone wine cellar with lit shelves"></div>
  </section>

  <section class="about">
    <p>Rvt studios has offered complete design services for residential and commercial projects for over 25 years. Our diversity has allowed RVT studios to design new construction and renovation projects in New York, California, Florida, Arizona and Mexico.</p>
    <p>we can work with your builder to coordinate the many architectural details required to create your personal space. Thus allowing your project to progress smoothly and more cost effectively.</p>
  </section>

  <svg class="footer-shapes" width="1200" height="72" viewBox="0 0 1200 72" aria-hidden="true">
    <polygon points="0,0 366,0 338,72 0,72" fill="var(--brown-tan)"/>
    <polygon points="373,0 1200,0 1200,72 345,72" fill="var(--brown-dark)"/>
  </svg>

  <div class="contact contact-phone">
    <svg width="38" height="38" viewBox="0 0 38 38" aria-hidden="true">
      <circle cx="19" cy="19" r="17" fill="none" stroke="#fff" stroke-width="2"/>
      <path d="M14 10c-2 1-3 3-2 6 1 5 5 10 9 12 2 1 4 0 5-1l-3-4-2 1c-2-1-4-4-5-6l1-2z" fill="none" stroke="#fff" stroke-width="2" stroke-linejoin="round"/>
    </svg>
    <span>402-555-0148</span>
  </div>
  <div class="contact contact-email">
    <svg width="38" height="26" viewBox="0 0 38 26" aria-hidden="true">
      <rect x="1" y="1" width="36" height="24" fill="#fff"/>
      <path d="M1 1l18 14L37 1" fill="none" stroke="var(--brown-dark)" stroke-width="2"/>
    </svg>
    <span>info@rvtstudios.com</span>
  </div>
  <div class="contact contact-web">
    <svg width="34" height="34" viewBox="0 0 34 34" aria-hidden="true" fill="none" stroke="#fff" stroke-width="2">
      <circle cx="17" cy="17" r="15"/>
      <ellipse cx="17" cy="17" rx="7" ry="15"/>
      <path d="M2 17h30M5 9h24M5 25h24M17 2v30"/>
    </svg>
    <span>www.rvtstudios.com</span>
  </div>
</main>
</body>
</html>
```